VARNOLA SYSTEMS BUSINESS CARD DESIGN

WE WANT COMPLETE NEW DESIGN OF OUR BUSINESS CARD. WE ARE AN INTEGRATION COMPANY, WHERE WE INTEGRATE IOT/SMART SYSTEMS TO HOMES AND CORPORATE CUSTOMERS. WE SUPPLY AND INSTALL AUTOMATION PRODUCTS. THE FINAL DESIGN SHOULD COMMUNICATE TECHNOLOGY. THE CARD DESIGN SHOULD BE VERY IMPACT FULL. LOGO NEEDS TO BE THERE. IT WOULD NICE IF THE DESIGN WAS CLEAN. COLORS IS UP TO DESIGNER TO PLAY WITH, OR CAN STICK TO CORPORATE COLORS (FOLLOW LOGO). I HAVE ADDED FEW REFERENCE PHOTOS TO DRAW INSPIRATION MAYBE. I HAVE ADDED A HEX DESIGN, ITS NOT NECESSARY TO USE THIS DESIGN, ITS UPTO DESIGNER, JUST ADDED IF NEEDED TO PLAY WITH DESIGN.

Target Market(s)

Private end users and corporate clients

Industry/Entity Type

technology, home automation, home theaters, building management systems, IOT

Contact Information for Business Card

It should include Employee name, personal number, office number, email address, both in English and arabic. DETAILS TO INCLUDE :GERALD MOSSANE, MOBILE 0097150738915,OFFCIE 009714386207, GERALD@VARNOLAHUB.CO

Requirements
Must have
• Should feel like a technology company from design. Details both and in English and arabic (or at least have provision for arabic in design).
Nice to have
• I would like logo on one side, and details on the other side. Logo design side should communicate technology with logo. Other side can be clean just with information or also have some design aspects following from logo side. it would be interesting to see submissions with square design as well (that looks like an app Icon). colors could be of logo, red black grey and white. I have added some designs to draw inspiration from

```html
<!DOCTYPE html>
<html lang="en">
<head>
<meta charset="utf-8">
<title>Varnola Systems Business Card</title>
<link href="https://fonts.googleapis.com/css2?family=Open+Sans:ital,wght@0,400;0,700;1,400&family=Noto+Naskh+Arabic:wght@400&family=Michroma&family=Roboto:wght@700&display=swap" rel="stylesheet">
<style>
  :root {
    --brand-red: #e31b23;
    --brand-red-deep: #d2171f;
    --ink: #231f20;
    --ink-soft: #333333;
    --paper: #ffffff;
    --stage-light: #ffffff;
    --stage-edge: #e4e4e4;
  }
  * { margin: 0; padding: 0; box-sizing: border-box; }
  html, body { width: 1200px; height: 515px; overflow: hidden; }
  body {
    position: relative;
    background: radial-gradient(ellipse at 50% 45%, var(--stage-light) 0%, #f3f3f3 55%, var(--stage-edge) 100%);
    font-family: "Open Sans", Arial, sans-serif;
  }
  .card {
    position: absolute;
    top: 104px;
    width: 464px;
    height: 283px;
    background: linear-gradient(135deg, var(--brand-red) 0%, var(--brand-red-deep) 50%, var(--brand-red) 100%);
  }
  .card::after {
    content: "";
    position: absolute;
    left: 20px; right: 20px; bottom: -10px;
    height: 14px;
    border-radius: 50%;
    background: rgba(0,0,0,0.18);
    filter: blur(7px);
    z-index: -1;
  }
  .card--front { left: 118px; }
  .card--back { left: 618px; color: var(--paper); }

  .front-panel {
    position: absolute;
    left: 16px; top: 15px;
    width: 432px; height: 252px;
    background: var(--paper);
  }
  .brand-lockup {
    position: absolute;
    left: 0; right: 0; top: 114px;
    display: flex; align-items: center; justify-content: center; gap: 10px;
  }
  .brand-square { width: 18px; height: 18px; background: var(--brand-red); }
  .brand-name {
    font-weight: 700; font-size: 27px; letter-spacing: 1px;
    color: var(--ink); line-height: 1;
  }
  .group-tagline {
    position: absolute;
    left: 0; right: 0; top: 225px;
    text-align: center;
    font-family: "Michroma", "Open Sans", sans-serif;
    font-size: 8.5px; letter-spacing: 1.6px;
    color: var(--ink);
  }
  .pattern-fill { position: absolute; inset: 0; }

  .contact-name {
    position: absolute; left: 0; right: 0; top: 82px;
    text-align: center; font-size: 13px; font-weight: 700;
  }
  .contact-name .role { font-weight: 400; font-style: italic; }
  .contact-name-ar {
    position: absolute; left: 0; right: 0; top: 98px;
    text-align: center; direction: rtl;
    font-family: "Noto Naskh Arabic", serif; font-size: 15px;
  }
  .contact-row {
    position: absolute; top: 124px; left: 0;
    font-size: 13.5px; line-height: 18px;
    display: flex; align-items: center; gap: 8px;
  }
  .contact-row--mobile { left: 74px; }
  .contact-row--email { left: 224px; }
  .contact-row svg { width: 11px; height: 11px; fill: var(--paper); }
  .divider {
    position: absolute; left: 145px; top: 203px;
    width: 172px; height: 1px; background: var(--ink);
  }
  .address {
    position: absolute; left: 62px; top: 209px;
    font-size: 13px; line-height: 18px;
    display: flex; align-items: center; gap: 7px; white-space: nowrap;
  }
  .address svg { width: 8px; height: 11px; fill: var(--paper); }
  .office-line {
    position: absolute; left: 0; right: 0; top: 233px;
    text-align: center; font-size: 13px; font-weight: 700;
  }

  .side-label {
    position: absolute; top: 420px; width: 200px;
    text-align: center;
    font-family: "Roboto", Arial, sans-serif; font-weight: 700;
    font-size: 15px; color: var(--ink-soft);
  }
  .side-label--front { left: 249px; }
  .side-label--back { left: 749px; }
</style>
</head>
<body>
  <section class="card card--front">
    <div class="pattern-fill" role="img" aria-label="Red geometric triangle pattern border"></div>
    <div class="front-panel">
      <div class="brand-lockup">
        <span class="brand-square"></span>
        <span class="brand-name">VARNOLA SYSTEMS</span>
      </div>
      <p class="group-tagline">A VARNOLA GROUP DIVISION.</p>
    </div>
  </section>

  <section class="card card--back">
    <div class="pattern-fill" role="img" aria-label="Red geometric triangle pattern background"></div>
    <p class="contact-name">Gerald Mossane, <span class="role">Director</span></p>
    <p class="contact-name-ar">جيرالد موسان ، مدير</p>
    <div class="contact-row contact-row--mobile">
      <svg viewBox="0 0 24 24" aria-hidden="true"><path d="M6.6 10.8a15.1 15.1 0 0 0 6.6 6.6l2.2-2.2c.3-.3.7-.4 1-.2 1.1.4 2.3.6 3.6.6.6 0 1 .4 1 1V20c0 .6-.4 1-1 1A17 17 0 0 1 3 4c0-.6.4-1 1-1h3.5c.6 0 1 .4 1 1 0 1.3.2 2.5.6 3.6.1.3 0 .7-.2 1z"/></svg>
      <span>0097150738915</span>
    </div>
    <div class="contact-row contact-row--email">
      <svg viewBox="0 0 24 24" aria-hidden="true"><path d="M2 5h20v14H2zm2 2v.5l8 5 8-5V7zm0 2.8V17h16V9.8l-8 5z"/></svg>
      <span>gerald@varnolahub.co</span>
    </div>
    <div class="divider"></div>
    <div class="address">
      <svg viewBox="0 0 16 22" aria-hidden="true"><path d="M8 0a8 8 0 0 0-8 8c0 6 8 14 8 14s8-8 8-14a8 8 0 0 0-8-8zm0 11a3 3 0 1 1 0-6 3 3 0 0 1 0 6z"/></svg>
      <span>#312 Rashed Noor Building, Al Qusais Post Box 48270</span>
    </div>
    <p class="office-line">Office: 009714386207</p>
  </section>

  <p class="side-label side-label--front">FRONT</p>
  <p class="side-label side-label--back">BACK</p>
</body>
</html>
```